High end business card design for custom homebuilding company

Looking for a high end business card design that is unique and elegant. Can use embossing, foil printing, laser die cutting, or any high end printing technique or high end paper. Will upload current design so you can see the logo and what we are using currently, but we want something more unique and elegant. I included our logo to help with design.

Target Market(s)

High end custom home buyers of $1.5 million plus homes. Also real estate developers of high end communities.

Industry/Entity Type

Business

Contact Information for Business Card

Double sided. We want something very elegant and expensive looking. We are looking to incorporate a combination of perhaps linen paper or a high end paper, with foil stamping or embossing/debossing to make the card look unique, but still elegant. We tend to use blacks and golds, but are open to any ideas. Looking for creative and unique design.

Colors

Designer to choose colors to be used in the design.

Requirements
Must have
• High end, elegant look. Can use foil, embossing, or high end papers like linen. We want to make the card unique and interesting, but elegant and expensive looking.
Nice to have
• I am including just some cards I saw that looked interesting for one reason or another. I like a clean elegant design and like both the clean white style, and the blacks. So not sure if we want a black design or white. Would like to see both.

```html
<!DOCTYPE html>
<html lang="en">
<head>
<meta charset="utf-8">
<title>Harbor Ridge Homes – Business Card</title>
<link rel="stylesheet" href="https://fonts.googleapis.com/css2?family=Open+Sans:wght@400;600;700&display=swap">
<style>
  :root {
    --backdrop: #2a2a2a;
    --card: #141414;
    --card-back: #181818;
    --deboss: #0b0b0b;
    --deboss-edge: #232323;
    --gold: #e6d33c;
    --gold-line: #b9a930;
    --text-light: #c9c9c9;
    --white: #ffffff;
  }
  * { box-sizing: border-box; margin: 0; padding: 0; }
  html, body {
    width: 1200px; height: 1000px; overflow: hidden;
    background: var(--backdrop);
    font-family: "Open Sans", Arial, sans-serif;
  }
  .canvas {
    position: relative; width: 1200px; height: 1000px;
  }
  .card {
    position: absolute; left: 220px; width: 760px; height: 434px;
    box-shadow: 0 18px 40px rgba(0,0,0,.55);
  }
  .card--front { top: 50px; background: var(--card); }
  .card--back { top: 516px; background: var(--card-back); }

  /* front */
  .front-brand {
    position: absolute; left: 0; right: 0; top: 150px;
    display: flex; align-items: center; justify-content: center; gap: 18px;
  }
  .brand-dot {
    width: 56px; height: 56px; border-radius: 50%;
  }
  .front-brand .brand-dot {
    background: var(--deboss);
    box-shadow: inset 1px 1px 2px #000, 1px 1px 0 var(--deboss-edge);
  }
  .front-brand .brand-name {
    font-weight: 600; font-size: 50px; letter-spacing: 4px; text-transform: uppercase;
    color: var(--deboss);
    text-shadow: 1px 1px 0 var(--deboss-edge);
  }
  .social {
    display: flex; gap: 9px; list-style: none;
  }
  .social li {
    width: 22px; height: 22px; border-radius: 50%; background: var(--gold);
  }
  .front-social { position: absolute; left: 380px; top: 300px; }

  /* back */
  .holder-name {
    position: absolute; left: 60px; top: 212px;
    color: var(--gold); font-weight: 700; font-size: 21px; letter-spacing: .5px;
  }
  .contact {
    position: absolute; left: 470px; top: 40px; width: 270px;
    color: var(--text-light); font-size: 14.5px; line-height: 20px;
  }
  .contact address { font-style: normal; margin-bottom: 16px; }
  .contact-row { display: flex; align-items: center; gap: 8px; }
  .contact-group { margin-bottom: 14px; }
  .contact-icon { width: 12px; height: 12px; flex: none; }
  .contact-icon.blank { visibility: hidden; }
  .back-social { margin-top: 2px; }
  .back-rule {
    position: absolute; left: 460px; right: 40px; top: 272px;
    height: 2px; background: var(--gold-line);
  }
  .back-brand {
    position: absolute; right: 40px; top: 318px;
    display: flex; align-items: center; gap: 12px;
  }
  .back-brand .brand-dot { width: 40px; height: 40px; background: var(--gold); }
  .back-brand .brand-name {
    color: var(--white); font-weight: 600; font-size: 30px; letter-spacing: 3px; text-transform: uppercase;
  }
</style>
</head>
<body>
<main class="canvas">
  <section class="card card--front" aria-label="Card front">
    <div class="front-brand">
      <span class="brand-dot"></span>
      <span class="brand-name">Harbor Ridge Homes</span>
    </div>
    <ul class="social front-social" aria-label="Social links">
      <li></li><li></li><li></li><li></li><li></li>
    </ul>
  </section>

  <section class="card card--back" aria-label="Card back">
    <p class="holder-name">MASON REID</p>
    <div class="contact">
      <address>Unit 4 18-22 Fenwick Street,<br>Belmont, WA 6104</address>
      <div class="contact-group">
        <div class="contact-row">
          <svg class="contact-icon" viewBox="0 0 12 12"><circle cx="6" cy="6" r="6" fill="var(--gold)"/><path d="M4 3l1.2 1.6-.7.8a4 4 0 0 0 2.1 2.1l.8-.7L9 8l-.7 1C5.5 9 3 6.5 3 3.7z" fill="#181818"/></svg>
          <span>00 0000 0000</span>
        </div>
        <div class="contact-row">
          <svg class="contact-icon" viewBox="0 0 12 12"><circle cx="6" cy="6" r="6" fill="var(--gold)"/><path d="M4 3l1.2 1.6-.7.8a4 4 0 0 0 2.1 2.1l.8-.7L9 8l-.7 1C5.5 9 3 6.5 3 3.7z" fill="#181818"/></svg>
          <span>00 0000 0000</span>
        </div>
      </div>
      <div class="contact-group">
        <div class="contact-row">
          <svg class="contact-icon" viewBox="0 0 12 12"><circle cx="6" cy="6" r="6" fill="var(--gold)"/><rect x="3" y="4" width="6" height="4.2" fill="none" stroke="#181818" stroke-width="1"/><path d="M3 4l3 2.3L9 4" fill="none" stroke="#181818" stroke-width="1"/></svg>
          <span>hello@harborridge.com.au</span>
        </div>
        <div class="contact-row">
          <svg class="contact-icon" viewBox="0 0 12 12"><circle cx="6" cy="6" r="6" fill="var(--gold)"/><circle cx="6" cy="6" r="3" fill="none" stroke="#181818" stroke-width="1"/><path d="M3 6h6M6 3v6" stroke="#181818" stroke-width=".8"/></svg>
          <span>www.harborridgehomes.com.au</span>
        </div>
      </div>
      <ul class="social back-social" aria-label="Social links">
        <li></li><li></li><li></li><li></li><li></li>
      </ul>
    </div>
    <div class="back-rule"></div>
    <div class="back-brand">
      <span class="brand-dot"></span>
      <span class="brand-name">Harbor Ridge Homes</span>
    </div>
  </section>
</main>
</body>
</html>
```